BrambleWorks business card

Looking for business card design that supports our company/software values. We have 2 logo designs at the moment but open to change if you think you can enhance the brand. Check out website www.brambleworks.com.au.

Target Market(s)

Education

Contact Information for Business Card

Name, title, mobile, email and website

Font styles to use
Sans Serif

Colors

Designer to choose colors to be used in the design.

Requirements
Must have
• BrambleWorks logo with tree and tagline on rear side with dark grey background colour

```html
<!DOCTYPE html>
<html lang="en">
<head>
<meta charset="utf-8">
<title>BrambleWorks business card</title>
<link rel="stylesheet" href="https://fonts.googleapis.com/css2?family=Montserrat:wght@400;700&family=Open+Sans:wght@400&display=swap">
<style>
  :root {
    --backdrop: #3a3431;
    --card: #1b1b1b;
    --card-edge: #111111;
    --wordmark-grey: #5a5a5a;
    --tagline-grey: #4d4d4d;
    --rule-grey: #3c3c3c;
    --accent: #f5b21b;
    --contact-grey: #6b6b6b;
    --foliage-dark: #262626;
    --foliage-light: #2f2f2f;
  }
  * { box-sizing: border-box; margin: 0; padding: 0; }
  html, body {
    width: 1200px;
    height: 716px;
    overflow: hidden;
    background: var(--backdrop);
  }
  .sheet {
    position: relative;
    width: 1200px;
    height: 716px;
  }
  .card {
    position: absolute;
    top: 204px;
    width: 540px;
    height: 308px;
    background: var(--card);
    border: 1px solid var(--card-edge);
    border-radius: 4px;
    box-shadow: 0 14px 30px rgba(0,0,0,0.45);
    overflow: hidden;
  }
  .card--front { left: 40px; }
  .card--back { left: 620px; }

  .branch-art {
    position: absolute;
    border-radius: 50%;
    background: radial-gradient(ellipse at center, var(--foliage-light) 0%, var(--foliage-dark) 55%, rgba(27,27,27,0) 75%);
  }
  .card--front .branch-art { right: -40px; top: 40px; width: 230px; height: 150px; }
  .card--back .branch-art { left: -50px; top: -40px; width: 230px; height: 170px; }

  /* front */
  .brand-lockup {
    position: absolute;
    left: 70px;
    top: 100px;
    width: 330px;
    font-family: "Open Sans", sans-serif;
  }
  .brand-lockup__name {
    display: flex;
    align-items: center;
    gap: 12px;
    font-size: 44px;
    font-weight: 400;
    color: var(--wordmark-grey);
    letter-spacing: 0.5px;
    line-height: 1;
  }
  .brand-lockup__dot {
    width: 14px;
    height: 14px;
    border-radius: 50%;
    background: var(--wordmark-grey);
    flex: none;
  }
  .brand-lockup__rule {
    margin-top: 10px;
    height: 1px;
    background: var(--rule-grey);
  }
  .brand-lockup__tagline {
    margin-top: 6px;
    font-size: 17px;
    color: var(--tagline-grey);
    letter-spacing: 0.5px;
  }

  /* back */
  .brand-mark {
    position: absolute;
    left: 230px;
    top: 78px;
    font-family: "Montserrat", sans-serif;
    font-weight: 700;
    font-size: 24px;
    color: var(--accent);
  }
  .accent-tick {
    position: absolute;
    left: 92px;
    top: 128px;
    width: 3px;
    height: 20px;
    background: var(--accent);
    transform: skewX(-14deg);
  }
  .holder {
    position: absolute;
    left: 120px;
    top: 128px;
    font-family: "Montserrat", sans-serif;
  }
  .holder__name {
    font-size: 20px;
    font-weight: 700;
    color: var(--accent);
    letter-spacing: 0.4px;
  }
  .holder__title {
    margin-top: 2px;
    font-size: 12px;
    color: var(--contact-grey);
    letter-spacing: 0.5px;
  }
  .contact-list {
    position: absolute;
    left: 92px;
    top: 200px;
    list-style: none;
    font-family: "Montserrat", sans-serif;
    font-size: 13px;
    color: var(--contact-grey);
  }
  .contact-list__item {
    display: flex;
    align-items: center;
    gap: 10px;
    height: 22px;
  }
  .contact-list__icon {
    width: 14px;
    height: 14px;
    flex: none;
    fill: none;
    stroke: var(--accent);
    stroke-width: 1.3;
  }
  .contact-list__domain { color: var(--accent); font-weight: 700; }
</style>
</head>
<body>
<main class="sheet">

  <section class="card card--front" aria-label="Card front">
    <div class="branch-art" role="img" aria-label="Embossed willow branches decoration"></div>
    <div class="brand-lockup">
      <div class="brand-lockup__name"><span class="brand-lockup__dot"></span>BrambleWorks</div>
      <div class="brand-lockup__rule"></div>
      <div class="brand-lockup__tagline">Student Success Platform</div>
    </div>
  </section>

  <section class="card card--back" aria-label="Card back">
    <div class="branch-art" role="img" aria-label="Embossed willow branches decoration"></div>
    <div class="brand-mark">BrambleWorks</div>
    <span class="accent-tick"></span>
    <div class="holder">
      <p class="holder__name">DELIA HARCOURT</p>
      <p class="holder__title">Assistent Director</p>
    </div>
    <ul class="contact-list">
      <li class="contact-list__item">
        <svg class="contact-list__icon" viewBox="0 0 14 14"><rect x="4" y="1.5" width="6" height="11" rx="1"/><line x1="6.2" y1="10.5" x2="7.8" y2="10.5"/></svg>
        <span>022 555 014</span>
      </li>
      <li class="contact-list__item">
        <svg class="contact-list__icon" viewBox="0 0 14 14"><rect x="1.5" y="3" width="11" height="8"/><polyline points="1.5,3 7,8 12.5,3"/></svg>
        <span>delia@brambleworks.com.au</span>
      </li>
      <li class="contact-list__item">
        <svg class="contact-list__icon" viewBox="0 0 14 14"><circle cx="7" cy="7" r="5.5"/><ellipse cx="7" cy="7" rx="2.4" ry="5.5"/><line x1="1.5" y1="7" x2="12.5" y2="7"/></svg>
        <span>www.<span class="contact-list__domain">brambleworks.com</span>.au</span>
      </li>
    </ul>
  </section>

</main>
</body>
</html>
```